Business Card

I need a business card that really pops for a potential customer or person who refers a personal injury lead. I want to highlight our office locations, but only address that needs to be on the card is my office's main address. I want a sleek, modern and minimalist design.

```html
<!DOCTYPE html>
<html lang="en">
<head>
<meta charset="UTF-8">
<title>Lakecrest Injury Lawyers – Business Card</title>
<link rel="stylesheet" href="https://fonts.googleapis.com/css2?family=Poppins:wght@700&family=Arimo:wght@400&display=swap">
<style>
  :root {
    --page-bg: #e6e3e3;
    --card-top: #eee7e7;
    --card-top-deep: #e0d3d3;
    --wave-dark: #3d3d3d;
    --wave-light: #7a7a7a;
    --ink-dark: #3a3a3a;
    --ink-light: #ffffff;
  }
  * { margin: 0; padding: 0; box-sizing: border-box; }
  html, body {
    width: 1200px;
    height: 900px;
    overflow: hidden;
    background: var(--page-bg);
  }
  .business-card {
    position: absolute;
    left: 100px;
    top: 141px;
    width: 1000px;
    height: 618px;
    overflow: hidden;
    background: linear-gradient(160deg, var(--card-top) 0%, var(--card-top-deep) 55%, var(--card-top) 100%);
    box-shadow: 0 18px 40px rgba(0, 0, 0, 0.18);
  }
  .card-wave {
    position: absolute;
    inset: 0;
    width: 1000px;
    height: 618px;
  }
  .wave-band { fill: var(--wave-light); }
  .wave-body { fill: var(--wave-dark); }

  .firm-name {
    position: absolute;
    left: 58px;
    top: 128px;
    color: var(--ink-dark);
    font-family: "Arimo", "Arial", sans-serif;
    font-weight: 400;
    font-size: 46px;
    line-height: 1.2;
    letter-spacing: normal;
  }

  .person {
    position: absolute;
    left: 58px;
    top: 424px;
    color: var(--ink-light);
  }
  .person__name {
    font-family: "Poppins", "Arial", sans-serif;
    font-weight: 700;
    font-size: 42px;
    line-height: 1.1;
  }
  .person__role {
    font-family: "Arimo", "Arial", sans-serif;
    font-weight: 400;
    font-size: 27px;
    line-height: 1.2;
    margin-top: 2px;
    margin-left: 2px;
  }

  .contact-list {
    position: absolute;
    right: 69px;
    top: 363px;
    list-style: none;
    color: var(--ink-light);
    font-family: "Arimo", "Arial", sans-serif;
    font-size: 27px;
  }
  .contact-list__item {
    display: flex;
    align-items: center;
    justify-content: flex-end;
    height: 36.5px;
  }
  .contact-list__icon {
    width: 26px;
    height: 26px;
    margin-left: 18px;
    fill: none;
    stroke: var(--ink-light);
    stroke-width: 1.8;
  }
  .office-address {
    position: absolute;
    right: 69px;
    top: 490px;
    text-align: right;
    font-style: normal;
    color: var(--ink-light);
    font-family: "Arimo", "Arial", sans-serif;
    font-size: 27px;
    line-height: 36px;
  }
</style>
</head>
<body>
  <main class="business-card">
    <svg class="card-wave" viewBox="0 0 1000 618" aria-hidden="true">
      <path class="wave-band" d="M0,312 C150,350 300,390 490,305 C650,240 840,248 1000,312 V618 H0 Z"/>
      <path class="wave-body" d="M0,350 C150,390 300,382 500,314 C670,256 850,262 1000,318 V618 H0 Z"/>
    </svg>

    <h1 class="firm-name">Lakecrest Injury Lawyers</h1>

    <section class="person">
      <h2 class="person__name">DANIEL HARPER</h2>
      <p class="person__role">Managing Director</p>
    </section>

    <ul class="contact-list">
      <li class="contact-list__item">044-555 018 273
        <svg class="contact-list__icon" viewBox="0 0 24 24" aria-hidden="true">
          <path d="M5 3h4l2 5-2.5 1.5a11 11 0 0 0 6 6L16 13l5 2v4a2 2 0 0 1-2 2A17 17 0 0 1 3 5a2 2 0 0 1 2-2z"/>
        </svg>
      </li>
      <li class="contact-list__item">info@lakecrestlaw.com
        <svg class="contact-list__icon" viewBox="0 0 24 24" aria-hidden="true">
          <rect x="2.5" y="5" width="19" height="14"/>
          <path d="M2.5 5l9.5 8 9.5-8M2.5 19l7-6.5M21.5 19l-7-6.5"/>
        </svg>
      </li>
      <li class="contact-list__item">www.lakecrestlaw.com
        <svg class="contact-list__icon" viewBox="0 0 24 24" aria-hidden="true">
          <circle cx="12" cy="12" r="9.5"/>
          <ellipse cx="12" cy="12" rx="4.5" ry="9.5"/>
          <path d="M2.5 12h19M4 7h16M4 17h16"/>
        </svg>
      </li>
    </ul>

    <address class="office-address">421, Address line goes<br>here 45452,Country Name</address>
  </main>
</body>
</html>
```